Milo Fenwick - Cinematographer

NEED:
I'm looking for a sleek, professional, modern business card that will give give the recipient the impression that they can trust their production will go smoothly by hiring me. I will bring creativity and knowledge to their shoot, so that we can create powerful images.
I am looking for a card with a strong style and design ethos that could be expanded to a website and a full visual/graphic/design entity for me.
ABOUT ME:
I am a mid-twenties cinematographer, I work on music video, narrative short, commercial, and corporate projects. I blend the science and artistry of cameras and filmmaking to tell a story. I'm an artist, a technician, and a manager.
DESIGN:
I like sleek, simple design. Black, dark grays, white, dark navy, steel blues, I love cyan, but also cyan and red. I am not a fan of earthy tones. I generally prefer modern, san-serif fonts over serifs. My old logo was based on an aperture, a multi-blade device at the back of a lens that controls how much light passes through, but I made it with so many colors, that it doesn't necessarily lend itself to a specific color-scheme or design ethos. I liked that the aperture design provided a sense of the technical requirements of my job. I'm a fan of matte business cards, but am open to plenty of specialty print processes to make an outstanding card.
ATTACHED FILES:
My Old Rainbox Aperture Logo, plus a few designs I've tried playing around with, but am not tied to. I AM OPEN TO NEW DESIGNS, DO NOT FEEL TIED TO THIS.
**I've pulled my old logo down from the attached files, and instead attached other business cards I like, so as not to mislead you where I would like to go.
INFO:
Name: Milo Fenwick
Job: Cinematographer
Email: mpfenwick@quellbox.net
Phone: 415.555.0193
Website: milofenwick.net
I'm adding some images of other cards that I like, and removing my old logo, since I'm looking for something new, and don't want that old logo to push anyone a certain direction.

```html
<!DOCTYPE html>
<html lang="en">
<head>
<meta charset="utf-8">
<title>Milo Fenwick – Cinematographer</title>
<link rel="stylesheet" href="https://fonts.googleapis.com/css2?family=Fira+Sans+Condensed:wght@300;500;600&family=Fira+Sans+Extra+Condensed:wght@800&display=swap">
<style>
  :root {
    --page: #e4e7e2;
    --card: #f3f4f1;
    --ink: #151515;
    --ink-soft: #2b2b2b;
    --ring: #4f5a59;
    --ring-edge: #ffffff;
    --photo-light: #e3e9ec;
    --photo-dark: #8d9ca4;
  }
  html, body {
    margin: 0;
    width: 1200px;
    height: 1000px;
    overflow: hidden;
    background: var(--page);
  }
  .canvas {
    position: relative;
    width: 1200px;
    height: 1000px;
  }
  .card {
    position: absolute;
    left: 293px;
    top: 309px;
    width: 680px;
    height: 391px;
    background: var(--card);
    border-radius: 8px;
    box-shadow: 0 2px 10px rgba(0,0,0,0.08);
  }
  .identity {
    position: absolute;
    left: 40px;
    top: 70px;
    width: 300px;
    text-align: center;
    color: var(--ink);
  }
  .brand-mark {
    display: flex;
    align-items: center;
    justify-content: center;
    height: 86px;
    font-family: "Fira Sans Condensed", sans-serif;
    font-weight: 600;
    font-size: 17px;
    color: var(--ink-soft);
  }
  .name {
    margin: 6px 0 0;
    font-family: "Fira Sans Extra Condensed", sans-serif;
    font-weight: 800;
    font-size: 39px;
    line-height: 1;
    letter-spacing: 0.2px;
    text-transform: uppercase;
  }
  .role {
    margin: 2px 0 0;
    font-family: "Fira Sans Condensed", sans-serif;
    font-weight: 500;
    font-size: 25px;
    line-height: 1.2;
  }
  .contact {
    margin: 20px 0 0;
    font-family: "Fira Sans Condensed", sans-serif;
    font-weight: 300;
    font-size: 24px;
    line-height: 33px;
  }
  .portrait {
    position: absolute;
    left: 369px;
    top: 67px;
    width: 272px;
    height: 272px;
  }
</style>
</head>
<body>
<main class="canvas">
  <section class="card">
    <div class="identity">
      <div class="brand-mark">Milo Fenwick</div>
      <h1 class="name">Milo Fenwick</h1>
      <p class="role">Cinematographer</p>
      <p class="contact">mpfenwick@quellbox.net<br>415.555.0193</p>
    </div>
    <svg class="portrait" viewBox="0 0 272 272">
      <defs>
        <linearGradient id="photoTone" x1="0" y1="0" x2="1" y2="1">
          <stop offset="0" stop-color="var(--photo-light)"/>
          <stop offset="1" stop-color="var(--photo-dark)"/>
        </linearGradient>
      </defs>
      <circle cx="136" cy="136" r="136" fill="var(--ring)"/>
      <circle cx="136" cy="136" r="104" fill="var(--ring-edge)"/>
      <circle cx="136" cy="136" r="100" fill="#111"/>
      <circle cx="136" cy="136" r="97.5" fill="url(#photoTone)" role="img" aria-label="Photo of a person working at a desk in a bright studio office"/>
    </svg>
  </section>
</main>
</body>
</html>
```